Sci Fi/ Secret Agent Author needs website design!

My name is Tamsin Roark and I am an author. I require a site that can provide information about myself and my books and other works.

I would like it to have a Home, blog function, (about the) books/series section so people can visit another section and read about each individual book that's going to be released. A resources page, a Store, social media links and ability to load/embed videos from vidorra and other.

I write mild scifi/thriller/conspiracy/secret government type novels. -At the moment-. The series follows a strong female lead that is an agent with a secret organisation in a classified military installation.

The theme would be professional yet possibly show this element.

Target Market(s)

/military fiction/thriller/fantasy/Sci fi/ femme-fatal, readers. Mostly females, age 18-60
Novel readers

Number of Pages Required

5+ page

Requirements
Must have
• Would like designers to follow brief. :)
• My budget includes all the pages I will need;
• eg home, blog, resources, store, ability to pay with quidlo and Credit Cards
• , ability to have trailers from vidorra etc. Must have links to the social media mentioned in the brief.
Nice to have
• use of the colours I have suggested. electric/indigo purple, fuschia highlights , dark greys
• as I will possibly base branding for social media ETC on the look of your website design and colour scheme.
• Ability for trailer on front page??
Should not have
• Should not be too cluttered. (But I am open to all ideas)

```html
<!DOCTYPE html>
<html lang="en">
<head>
<meta charset="utf-8">
<title>Tamsin Roark – Other Works</title>
<link rel="stylesheet" href="https://fonts.googleapis.com/css2?family=Roboto+Condensed:wght@400;700&family=Open+Sans:wght@400;600&display=swap">
<style>
:root{
  --purple:#5e12a6;
  --purple-deep:#4a0c8a;
  --purple-bright:#7a1fd0;
  --band-top:#6a2fd6;
  --band-bottom:#8d3bd8;
  --ink:#333;
  --muted:#666;
  --light:#f3f3f3;
  --dark:#262626;
  --white:#fff;
}
*{margin:0;padding:0;box-sizing:border-box}
html,body{width:740px;height:1200px;overflow:hidden;background:var(--white)}
body{position:relative;font-family:'Open Sans',sans-serif;color:var(--ink)}
.abs{position:absolute}
.cond{font-family:'Roboto Condensed',sans-serif}

.site-header{left:0;top:0;width:740px;height:59px;background:var(--purple)}
.brand{left:60px;top:15px;font:700 25px/1 'Roboto Condensed',sans-serif;color:var(--white);letter-spacing:.5px}
.main-nav{left:254px;top:25px;display:flex;gap:19px;font:400 9px/1 'Roboto Condensed',sans-serif;color:var(--white);text-transform:uppercase}
.header-social{left:628px;top:25px;display:flex;gap:4px}
.header-social span{width:7px;height:7px;border-radius:50%;background:var(--white);display:block}

.hero{left:0;top:59px;width:740px;height:230px}
.hero-title{left:0;top:126px;width:740px;text-align:center;font:400 26px/1 'Roboto Condensed',sans-serif;color:var(--white);letter-spacing:.5px}
.hero-sub{left:0;top:162px;width:740px;text-align:center;font:400 9.5px/16px 'Roboto Condensed',sans-serif;color:var(--white)}

.intro{left:90px;top:341px;width:560px;text-align:center;font-size:7.4px;line-height:13.6px;color:var(--ink)}

.card{top:413px;width:196px;text-align:center}
.card-photo{width:196px;height:118px;display:block}
.card-title{margin-top:16px;font-size:12px;color:var(--ink)}
.card-text{margin-top:8px;font-size:6.6px;line-height:12.8px;color:var(--muted)}
.read-more{display:inline-block;margin-top:9px;border:1px solid #555;padding:4px 5px;font:400 6.5px/1 'Open Sans',sans-serif;color:var(--ink);text-transform:uppercase}

.newsletter{left:0;top:677px;width:740px;height:307px;background:linear-gradient(180deg,var(--band-top),var(--band-bottom))}
.video-frame{left:88px;top:741px;width:285px;height:184px;border:3px solid #ddd;background:linear-gradient(160deg,#2b3f58,#12202f 60%,#0b141d)}
.play{left:213px;top:825px;width:28px;height:18px;background:#d91c1c;border-radius:3px}
.news-title{left:407px;top:752px;font:700 19px/1 'Roboto Condensed',sans-serif;color:var(--white)}
.news-text{left:407px;top:779px;width:250px;font-size:6.6px;line-height:11.6px;color:var(--white);font-weight:600}
.field{left:408px;width:240px;height:25px;background:var(--white);font-size:6.8px;color:#555;display:flex;align-items:center;justify-content:center}
.subscribe{left:408px;top:887px;width:240px;height:26px;background:var(--dark);color:var(--white);font:400 11px/26px 'Roboto Condensed',sans-serif;text-align:center}

.site-footer{left:0;top:984px;width:740px;height:178px;background:var(--light)}
.foot-brand{left:60px;top:1016px;font:700 25px/1 'Roboto Condensed',sans-serif;color:var(--purple-bright)}
.foot-about{left:60px;top:1050px;width:190px;font-size:7px;line-height:12.8px;color:var(--ink)}
.foot-head{font:400 12px/1 'Roboto Condensed',sans-serif;color:var(--ink);text-transform:uppercase}
.contact-list{left:292px;top:1041px;font-size:7.5px;color:var(--ink);line-height:12.8px}
.contact-list li{list-style:none;display:flex;gap:8px;margin-bottom:6px}
.contact-list svg{flex:none;margin-top:2px}
.links{left:486px;top:1040px;font-size:6.6px;line-height:12.7px;color:var(--ink)}
.links li{list-style:none;padding-left:12px;position:relative}
.links li::before{content:"";position:absolute;left:2px;top:4px;border-left:3px solid #333;border-top:2.5px solid transparent;border-bottom:2.5px solid transparent}
.social-list{left:615px;top:1041px;font-size:8.5px;color:#444}
.social-list li{list-style:none;display:flex;align-items:center;gap:6px;height:20.8px}
.social-list li span{width:15px;height:15px;border:1px solid #555;border-radius:50%;display:block}
.footer-rule{left:0;top:1162px;width:740px;height:1px;background:#ddd}
.copyright{left:0;top:1176px;width:740px;text-align:center;font-size:6.6px;color:var(--ink)}
</style>
</head>
<body>

<header class="site-header abs">
  <div class="brand abs">TAMSIN ROARK</div>
  <nav class="main-nav abs">
    <span>Home</span><span>Books</span><span>Blog</span><span>Resources</span><span>Other Works</span><span>Store</span><span>Contact Us</span>
  </nav>
  <div class="header-social abs" aria-label="Social links">
    <span></span><span></span><span></span><span></span><span></span>
  </div>
</header>

<svg class="hero abs" viewBox="0 0 740 230" role="img" aria-label="Photo of hands typing on a laptop in a dim office">
  <defs>
    <linearGradient id="heroShade" x1="0" y1="0" x2="1" y2="0.4">
      <stop offset="0" stop-color="#5b4a32"/>
      <stop offset=".45" stop-color="#3a3a30"/>
      <stop offset="1" stop-color="#141310"/>
    </linearGradient>
  </defs>
  <rect width="740" height="230" fill="url(#heroShade)"/>
  <path d="M0 206 Q370 290 740 206 L740 230 L0 230 Z" fill="var(--purple-bright)"/>
  <path d="M0 210 Q370 292 740 212 L740 230 L0 230 Z" fill="#fff"/>
</svg>
<h1 class="hero-title abs">OTHER WORKS</h1>
<p class="hero-sub abs">SED UT PERSPICIATIS UNDE OMNIS ISTE NATUS ERROR SIT VOLUPTATEM<br>ACCUSANTIUM DOLOREMQUE LAUDANTIUM, TOTAM REM</p>

<p class="intro abs">Sed ut perspiciatis unde omnis iste natus error sit voluptatem accusantium doloremque laudantium, totam rem aperiam, eaque ipsa quae ab illo inventore veritatis et quasi architecto beatae vitae dicta sunt explicabo. Nemo enim ipsam voluptatem quia voluptas sit aspernatur aut odit aut fugit, sed quia cousntur magni dolores eos qui ratione voluptatem sequi nesciunt. Neque porro quisquam est, qui dolorem ipsum</p>

<article class="card abs" style="left:61px">
  <svg class="card-photo" viewBox="0 0 196 118" role="img" aria-label="Photo of a woman reading a book">
    <path d="M0 6 Q0 0 6 0 H190 Q196 0 196 6 V100 Q98 130 0 100 Z" fill="#7a5a32"/>
  </svg>
  <h2 class="card-title">Duis aute irure dolor in</h2>
  <p class="card-text">Sed ut perspiciatis unde omnis iste natus error sit voluptatem accusantium doloremque laudantium, totam rem aperiam, eaque ipsa quae ab illo inventore veritatis</p>
  <span class="read-more">Read more ⊕</span>
</article>
<article class="card abs" style="left:272px">
  <svg class="card-photo" viewBox="0 0 196 118" role="img" aria-label="Photo of hands on a laptop keyboard at a desk">
    <path d="M0 6 Q0 0 6 0 H190 Q196 0 196 6 V100 Q98 130 0 100 Z" fill="#6f7a82"/>
  </svg>
  <h2 class="card-title">Duis aute irure dolor in</h2>
  <p class="card-text">Sed ut perspiciatis unde omnis iste natus error sit voluptatem accusantium doloremque laudantium, totam rem aperiam, eaque ipsa quae ab illo inventore veritatis</p>
  <span class="read-more">Read more ⊕</span>
</article>
<article class="card abs" style="left:483px">
  <svg class="card-photo" viewBox="0 0 196 118" role="img" aria-label="Photo of a woman writing in a library">
    <path d="M0 6 Q0 0 6 0 H190 Q196 0 196 6 V100 Q98 130 0 100 Z" fill="#4e5a62"/>
  </svg>
  <h2 class="card-title">Duis aute irure dolor in</h2>
  <p class="card-text">Sed ut perspiciatis unde omnis iste natus error sit voluptatem accusantium doloremque laudantium, totam rem aperiam, eaque ipsa quae ab illo inventore veritatis</p>
  <span class="read-more">Read more ⊕</span>
</article>

<section class="newsletter abs" role="img" aria-label="Purple tinted photo of a desert road"></section>
<div class="video-frame abs" role="img" aria-label="Book trailer video still of a woman reading in a dark library"></div>
<div class="play abs"></div>
<svg class="abs" style="left:244px;top:829px" width="10" height="10" viewBox="0 0 10 10"><path d="M0 0 L10 5 L0 10 Z" fill="#fff" transform="translate(-7 -0)"/></svg>
<svg class="abs" style="left:106px;top:898px" width="190" height="6" viewBox="0 0 190 6"><rect width="190" height="4" y="1" fill="#555"/><rect width="84" height="4" y="1" fill="#c8181b"/></svg>

<h2 class="news-title abs">SIGN UP FOR OUR NEWSLETTER</h2>
<p class="news-text abs">Sed ut perspiciatis unde omnis iste natus error sit voluptatem accusantium doloremque laudantium, totam rem aperiam, eaque ipsa quae ab illo inventore veritatis et quasi architecto beatae vitae dicta sunt explicabo</p>
<div class="field abs" style="top:825px">Enter Name</div>
<div class="field abs" style="top:857px">Enter Email</div>
<div class="subscribe abs">SUBSCRIBE</div>

<footer class="site-footer abs"></footer>
<div class="foot-brand abs">TAMSIN ROARK</div>
<p class="foot-about abs">Sed ut perspiciatis unde omnis iste natus error sit voluptatem accusantium doloremque lauantium, totam rem aperiam, eaque ipsa quae ab illo inventore veritatis et quasi architecto beatae vitae dicta sunt explicabo</p>

<h3 class="foot-head abs" style="left:292px;top:1017px">Contact Us</h3>
<ul class="contact-list abs">
  <li><svg width="9" height="11" viewBox="0 0 9 11"><path d="M4.5 10.5 C1 6.5 .5 5 .5 4 a4 4 0 0 1 8 0 c0 1-.5 2.5-4 6.5Z" fill="none" stroke="#444"/><circle cx="4.5" cy="4" r="1.4" fill="#444"/></svg><span>Tamsin Roark<br>Harbour Lane 12, 40211 Norwell</span></li>
  <li><svg width="9" height="9" viewBox="0 0 9 9"><path d="M1 .5 L3 .5 L3.8 2.8 L2.6 3.8 Q3.6 5.6 5.2 6.4 L6.2 5.2 L8.5 6 L8.5 8 Q4 9 .5 3 Z" fill="#444"/></svg><span style="font-size:8.5px">Phone: +44 20 7946 0321</span></li>
  <li><svg width="9" height="7" viewBox="0 0 9 7"><rect width="9" height="7" fill="#444"/><path d="M0 0 L4.5 3.5 L9 0" fill="none" stroke="#fff" stroke-width=".8"/></svg><span>hello@tamsinroark.com</span></li>
</ul>

<h3 class="foot-head abs" style="left:486px;top:1015px">Quick Links</h3>
<ul class="links abs">
  <li>Home</li><li>About the book</li><li>Blog</li><li>Resources</li><li>Blog</li><li>store</li><li>Contact Us</li>
</ul>

<h3 class="foot-head abs" style="left:616px;top:1015px">Social</h3>
<ul class="social-list abs">
  <li><span></span>Gatherly</li>
  <li><span></span>Chirpline</li>
  <li><span></span>Snapframe</li>
  <li><span></span>Pinboardly</li>
  <li><span></span>vidorra</li>
</ul>

<div class="footer-rule abs"></div>
<p class="copyright abs">©2017 Tamsin Roark, All Rights Reserved.</p>

</body>
</html>
```